Solids Control Presentation Template Design

I'm putting together a technical 5-day course about solids control and waste management. I'm looking for an updated art and a easy on the eyes format.

```html
<!DOCTYPE html>
<html lang="en">
<head>
<meta charset="utf-8">
<title>Solids Control Course – Presentation Template</title>
<link href="https://fonts.googleapis.com/css2?family=Montserrat:wght@500;600;700;800&family=Oswald:wght@500;600;700&family=Poppins:wght@400;500&display=swap" rel="stylesheet">
<style>
:root{
  --bg:#0b0b0b;
  --paper:#ffffff;
  --ink:#1a1a1a;
  --body:#4a4a4a;
  --muted:#7a7a7a;
  --red:#9e3034;
  --maroon:#8b1a2e;
  --wine:#7a1a1f;
  --scarlet:#c41e1e;
  --orange:#c43a1e;
  --slate:#3b3b3b;
  --charcoal:#3a4247;
  --grey:#6e6e6e;
  --footer-dark:#231616;
  --card:#f7f5f2;
  --card-line:#d9a4a4;
  --grid:#e6e6e6;
}
*{margin:0;padding:0;box-sizing:border-box}
html,body{width:1200px;height:1022px;overflow:hidden;background:var(--bg)}
.stage{position:absolute;left:0;top:0;width:1480px;height:1260px;transform:scale(.8108);transform-origin:0 0;background:var(--bg)}
.slide{position:absolute;width:712px;height:400px;background:var(--paper);overflow:hidden;font-family:'Poppins',sans-serif;color:var(--body)}
.s1{left:14px;top:14px}.s2{left:746px;top:14px}
.s3{left:14px;top:430px}.s4{left:746px;top:430px}
.s5{left:14px;top:848px}.s6{left:746px;top:848px}
.slide-title{position:absolute;left:16px;top:16px;font-family:'Montserrat',sans-serif;font-weight:700;font-size:18.5px;color:var(--ink);letter-spacing:-.2px}
.slide-title span{color:var(--red)}
.brand{position:absolute;right:12px;top:14px;display:flex;align-items:center;gap:6px;font-family:'Montserrat',sans-serif;font-weight:800;font-size:19px;color:var(--ink);letter-spacing:1.5px}
.brand i{display:block;width:9px;height:9px;background:var(--red)}
.footer{position:absolute;left:0;bottom:0;width:712px;height:25px}
.footer svg{position:absolute;inset:0}
.footer .copy{position:absolute;left:9px;top:6px;font-size:9.5px;font-weight:500;color:#fff}
.footer .page{position:absolute;left:648px;top:6px;font-size:9.5px;font-weight:500;color:#fff}

/* slide 1 */
.info-heading{position:absolute;left:33px;top:84px;font-family:'Montserrat',sans-serif;font-weight:600;font-size:23px;color:var(--ink)}
.info-heading span{color:var(--red)}
.info-copy{position:absolute;left:35px;top:122px;width:279px;height:240px;overflow:hidden;font-size:7.5px;line-height:15.5px;text-align:justify}
.info-copy p+p{margin-top:15.5px}
.petal{position:absolute;width:148px;height:147px;border-radius:50%;color:#fff;text-align:center;padding:22px 20px 0}
.petal b{display:block;font-family:'Montserrat',sans-serif;font-weight:600;font-size:21px;margin-bottom:4px}
.petal p{font-size:7px;line-height:11.4px}
.p1{left:377px;top:74px;background:var(--maroon);border-bottom-right-radius:0}
.p2{left:526px;top:74px;background:var(--slate);border-bottom-left-radius:0}
.p3{left:377px;top:221px;background:var(--slate);border-top-right-radius:0}
.p4{left:526px;top:221px;background:var(--maroon);border-top-left-radius:0}

/* slide 2 */
.plan{position:absolute;top:100px;width:141px;height:237px;background:var(--card);border:1px solid var(--card-line);border-radius:10px;text-align:center}
.plan::after{content:"";position:absolute;left:62px;bottom:-8px;width:12px;height:12px;background:var(--card);border-right:1px solid var(--card-line);border-bottom:1px solid var(--card-line);transform:rotate(45deg)}
.plan .price{margin-top:16px;font-family:'Oswald',sans-serif;font-weight:600;font-size:25px;color:var(--ink)}
.plan .tier{position:absolute;left:-4px;right:-4px;top:60px;height:27px;line-height:27px;font-family:'Oswald',sans-serif;font-weight:600;font-size:8px;color:#fff}
.plan ul{list-style:none;position:absolute;left:0;right:0;top:101px;font-size:8.4px;color:var(--muted)}
.plan li{height:22px}
.pl1{left:49px}.pl1 .tier{background:var(--red)}
.pl2{left:210px}.pl2 .tier{background:var(--wine)}
.pl3{left:370px}.pl3 .tier{background:var(--scarlet)}
.pl4{left:531px}.pl4 .tier{background:var(--grey)}

/* slide 3 */
.flow{position:absolute;left:0;top:0}
.step{position:absolute;top:116px;width:124px;text-align:center}
.step h3{margin-top:10px;font-family:'Montserrat',sans-serif;font-weight:600;font-size:14px;color:var(--maroon)}
.step p{margin-top:6px;font-size:9px;line-height:15.7px;color:#555}
.step svg{display:block;margin:0 auto}
.st1{left:79px}.st2{left:298px}.st3{left:518px}
.st3 h3{color:var(--grey)}

/* slide 4 */
.graph-heading{position:absolute;left:38px;top:104px;font-family:'Montserrat',sans-serif;font-weight:600;font-size:24px;color:var(--ink)}
.graph-copy{position:absolute;left:38px;top:143px;width:250px;font-size:8.3px;line-height:17px;color:#555}
.graph-copy p+p{margin-top:17px}
.chart{position:absolute;left:0;top:0}
.chart text{font-family:'Poppins',sans-serif;font-weight:500;font-size:10px;fill:#333}

/* slide 5 */
.seg{position:absolute;width:200px}
.seg h4{font-family:'Montserrat',sans-serif;font-weight:700;font-size:11.5px;color:var(--red);margin-bottom:4px}
.seg p{font-size:7.6px;line-height:14px;color:var(--muted)}
.seg.left{left:22px;text-align:right}
.seg.right{left:478px;width:215px}
.sg1{top:115px}.sg2{top:115px}.sg3{top:238px}.sg4{top:238px}

/* slide 6 */
.row{position:absolute;left:44px;width:614px;height:82px}
.row .tag{position:absolute;left:0;top:0}
.row .tag span{position:absolute;left:18px;top:30px;font-family:'Oswald',sans-serif;font-weight:600;font-size:14px;color:#fff}
.row .panel{position:absolute;left:42px;top:6px;width:572px;height:71px;background:var(--card);border:1px solid #c9a9a9;border-radius:4px;padding:7px 18px;overflow:hidden}
.row h5{font-family:'Montserrat',sans-serif;font-weight:600;font-size:11.5px;color:var(--ink)}
.row p{font-size:7.2px;line-height:13.6px;color:#444;white-space:nowrap}
.r1{top:68px}.r2{top:164px}.r3{top:260px}
</style>
</head>
<body>
<div class="stage">

  <section class="slide s1">
    <h2 class="slide-title">INFOGRAPHICS <span>TITLE HERE</span></h2>
    <div class="brand"><i></i>KEENLINE</div>
    <h3 class="info-heading"><span>Infographics</span> Title here</h3>
    <div class="info-copy">
      <p>Lorem ipsum dolor sit amet, consect eturadi eturadi piscing elit, sed do eiusmod tempor incid idunt utlabore Lorem ipsum dolor sit amet, consect eturadi piscing elit, sed do piscing elit, sed do e sed do Lorem ipsum dolor sit amet, consect eturadi eturadi piscing elit, sed do eiusmod tempor incid idunt utlabore Lorem ipsum dolor sit amet, consect eturadi piscing elit, sed do piscing elit, sed do e</p>
      <p>Lorem ipsum dolor sit amet, consect eturadi eturadi piscing elit, sed do eiusmod tempor incid idunt utlabore Lorem ipsum dolor sit amet, consect eturadi piscing elit, sed do piscing elit, sed do e sed do Lorem ipsum dolor sit amet, consect eturadi eturadi piscing elit, sed do eiusmod tempor incid idunt utlabore Lorem ipsum dolor sit amet, consect eturadi piscing elit, sed do piscing elit, sed do e</p>
    </div>
    <div class="petal p1"><b>01</b><p>Lorem ipsum dolor sit amet, consect eturadi eturadi piscing elit, sed do eiusmod tempor incid idunt utlabore Lorem ipsum dolor sit amet, consect eturadi piscing elit,</p></div>
    <div class="petal p2"><b>02</b><p>Lorem ipsum dolor sit amet, consect eturadi eturadi piscing elit, sed do eiusmod tempor incid idunt utlabore Lorem ipsum dolor sit amet, consect eturadi piscing elit,</p></div>
    <div class="petal p3"><b>03</b><p>Lorem ipsum dolor sit amet, consect eturadi eturadi piscing elit, sed do eiusmod tempor incid idunt utlabore Lorem ipsum dolor sit amet, consect eturadi piscing elit,</p></div>
    <div class="petal p4"><b>04</b><p>Lorem ipsum dolor sit amet, consect eturadi eturadi piscing elit, sed do eiusmod tempor incid idunt utlabore Lorem ipsum dolor sit amet, consect eturadi piscing elit,</p></div>
    <footer class="footer"><svg width="712" height="25"><rect width="712" height="25" fill="var(--red)"/><polygon points="584,0 597,0 622,25 609,25" fill="#fff"/><polygon points="597,0 712,0 712,25 622,25" fill="var(--footer-dark)"/></svg><span class="copy">Copyright text here</span><span class="page">Page : 01</span></footer>
  </section>

  <section class="slide s2">
    <h2 class="slide-title">SECTION <span>TITLE HERE</span></h2>
    <div class="brand"><i></i>KEENLINE</div>
    <div class="plan pl1"><div class="price">$49</div><div class="tier">PERSONAL</div><ul><li>20 GB Bandwidth</li><li>Financ Analysing</li><li>Daily 15 Reports</li><li>12 Team Members</li><li>24 hour support</li></ul></div>
    <div class="plan pl2"><div class="price">$75</div><div class="tier">PROFESSIONAL</div><ul><li>20 GB Bandwidth</li><li>Financ Analysing</li><li>Daily 15 Reports</li><li>12 Team Members</li><li>24 hour support</li></ul></div>
    <div class="plan pl3"><div class="price">$85</div><div class="tier">SMALL BUSINESS</div><ul><li>20 GB Bandwidth</li><li>Financ Analysing</li><li>Daily 15 Reports</li><li>12 Team Members</li><li>24 hour support</li></ul></div>
    <div class="plan pl4"><div class="price">$99</div><div class="tier">STARTUP</div><ul><li>20 GB Bandwidth</li><li>Financ Analysing</li><li>Daily 15 Reports</li><li>12 Team Members</li><li>24 hour support</li></ul></div>
    <footer class="footer"><svg width="712" height="25"><rect width="712" height="25" fill="var(--red)"/><polygon points="584,0 597,0 622,25 609,25" fill="#fff"/><polygon points="597,0 712,0 712,25 622,25" fill="var(--footer-dark)"/></svg><span class="copy">Copyright text here</span><span class="page">Page : 01</span></footer>
  </section>

  <section class="slide s3">
    <h2 class="slide-title">SECTION <span>TITLE HERE</span></h2>
    <div class="brand"><i></i>KEENLINE</div>
    <svg class="flow" width="712" height="400" fill="none" stroke-width="4" stroke-linejoin="round">
      <path d="M222,155 L222,114 Q222,92 200,92 L82,92 Q60,92 60,114 L60,312 Q60,334 82,334 L200,334 Q222,334 222,312 L222,258 L283,165 L283,114 Q283,92 305,92 L420,92 Q442,92 442,114 L442,155" stroke="var(--maroon)"/>
      <path d="M283,270 L283,312 Q283,334 305,334 L420,334 Q442,334 442,312 L442,258 L503,165 L503,114 Q503,92 525,92 L642,92 Q664,92 664,114 L664,312 Q664,334 642,334 L525,334 Q503,334 503,312 L503,270" stroke="var(--grey)"/>
      <circle cx="222" cy="155" r="8.5" fill="var(--maroon)" stroke="none"/>
      <circle cx="442" cy="155" r="8.5" fill="var(--maroon)" stroke="none"/>
      <circle cx="283" cy="270" r="8.5" fill="var(--grey)" stroke="none"/>
      <circle cx="503" cy="270" r="8.5" fill="var(--grey)" stroke="none"/>
    </svg>
    <div class="step st1">
      <svg width="26" height="36" viewBox="0 0 26 36"><path d="M13,1 C6,1 1,6 1,13 C1,18 4,21 6,24 L6,27 L20,27 L20,24 C22,21 25,18 25,13 C25,6 20,1 13,1Z" fill="var(--maroon)"/><rect x="7" y="29" width="12" height="2.5" fill="var(--maroon)"/><rect x="9" y="33" width="8" height="2.5" rx="1" fill="var(--maroon)"/></svg>
      <h3>ICON HERE</h3>
      <p>Lorem ipsum dolor sit amet, consectetur adipi-scing elit, sed do eius-mod tempor incididunt ut labore et dolore magna aliqua.</p>
    </div>
    <div class="step st2">
      <svg width="36" height="36" viewBox="0 0 36 36"><rect x="3" y="9" width="30" height="19" fill="none" stroke="var(--maroon)" stroke-width="2.2"/><path d="M3,9 L18,21 L33,9 M3,28 L14,18 M33,28 L22,18" fill="none" stroke="var(--maroon)" stroke-width="2"/></svg>
      <h3>ICON HERE</h3>
      <p>Lorem ipsum dolor sit amet, consectetur adipi-scing elit, sed do eius-mod tempor incididunt ut labore et dolore magna aliqua.</p>
    </div>
    <div class="step st3">
      <svg width="36" height="36" viewBox="0 0 36 36"><path d="M5,5 L5,31 L32,31" fill="none" stroke="var(--grey)" stroke-width="2.6"/><path d="M9,26 L16,17 L20,21 L29,11" fill="none" stroke="var(--grey)" stroke-width="2.6"/><path d="M23,9 L31,9 L31,17" fill="none" stroke="var(--grey)" stroke-width="2.6"/></svg>
      <h3>ICON HERE</h3>
      <p>Lorem ipsum dolor sit amet, consectetur adipi-scing elit, sed do eius-mod tempor incididunt ut labore et dolore magna aliqua.</p>
    </div>
    <footer class="footer"><svg width="712" height="25"><rect width="712" height="25" fill="var(--red)"/><polygon points="584,0 597,0 622,25 609,25" fill="#fff"/><polygon points="597,0 712,0 712,25 622,25" fill="var(--footer-dark)"/></svg><span class="copy">Copyright text here</span><span class="page">Page : 01</span></footer>
  </section>

  <section class="slide s4">
    <h2 class="slide-title">SECTION <span>TITLE HERE</span></h2>
    <div class="brand"><i></i>KEENLINE</div>
    <h3 class="graph-heading">Graph title here</h3>
    <div class="graph-copy">
      <p>Lorem ipsum dolor sit amet, consectetur adipiscing elit, sed do eiusmod tempor incididunt ut labore et dolore magna aliqua. Quis ipsum suspendisse ultrices gravida. Risus commodo viverra maecenas accumsan lacus vel facilisis.</p>
      <p>Eiusmod tempor incididunt ut labore et dolore magna aliqua. Quis ipsum suspendisse ultrices gravida. Risus commodo viverra maecenas accumsan lacus vel facilisis.</p>
    </div>
    <svg class="chart" width="712" height="400">
      <g stroke="var(--grid)" stroke-width="1">
        <line x1="283" y1="138" x2="702" y2="138"/><line x1="283" y1="183" x2="702" y2="183"/>
        <line x1="283" y1="229" x2="702" y2="229"/><line x1="283" y1="274" x2="702" y2="274"/>
        <line x1="283" y1="318" x2="702" y2="318"/>
      </g>
      <g fill="#2a2a2a">
        <rect x="323" y="254" width="7" height="64"/><rect x="368" y="141" width="7" height="177"/>
        <rect x="415" y="147" width="7" height="171"/><rect x="461" y="127" width="7" height="191"/>
        <rect x="507" y="171" width="7" height="147"/><rect x="552" y="210" width="7" height="108"/>
        <rect x="600" y="102" width="7" height="216"/><rect x="646" y="138" width="7" height="180"/>
      </g>
      <g fill="var(--red)">
        <rect x="330" y="229" width="7" height="89"/><rect x="375" y="119" width="7" height="199"/>
        <rect x="422" y="183" width="7" height="135"/><rect x="468" y="113" width="7" height="205"/>
        <rect x="514" y="113" width="7" height="205"/><rect x="559" y="184" width="7" height="134"/>
        <rect x="607" y="80" width="7" height="238"/><rect x="653" y="113" width="7" height="205"/>
      </g>
      <g text-anchor="middle">
        <text x="331" y="342">2012</text><text x="376" y="342">2012</text><text x="423" y="342">2012</text><text x="468" y="342">2012</text>
        <text x="514" y="342">2012</text><text x="559" y="342">2012</text><text x="607" y="342">2012</text><text x="653" y="342">2012</text>
      </g>
    </svg>
    <footer class="footer"><svg width="712" height="25"><rect width="712" height="25" fill="var(--red)"/><polygon points="584,0 597,0 622,25 609,25" fill="#fff"/><polygon points="597,0 712,0 712,25 622,25" fill="var(--footer-dark)"/></svg><span class="copy">Copyright text here</span><span class="page">Page : 01</span></footer>
  </section>

  <section class="slide s5">
    <h2 class="slide-title">SECTION <span>TITLE HERE</span></h2>
    <div class="brand"><i></i>KEENLINE</div>
    <svg width="712" height="400" style="position:absolute;left:0;top:0" fill="none">
      <line x1="70" y1="181" x2="610" y2="181" stroke="var(--grid)"/>
      <g transform="rotate(-90 356 184)" stroke-width="19">
        <circle cx="356" cy="184" r="57" stroke="var(--charcoal)"/>
        <circle cx="356" cy="184" r="57" stroke="var(--red)" stroke-dasharray="60 299"/>
        <circle cx="356" cy="184" r="57" stroke="var(--orange)" stroke-dasharray="0 60 60 239"/>
        <circle cx="356" cy="184" r="57" stroke="#a8302e" stroke-dasharray="0 120 60 179"/>
      </g>
      <g stroke="#555" stroke-width="1">
        <polyline points="309,139 272,123 234,123"/><polyline points="411,149 444,123 476,123" stroke="var(--red)"/>
        <polyline points="299,219 271,246 234,246"/><polyline points="412,223 446,246 476,246" stroke="var(--red)"/>
      </g>
      <g fill="#fff" stroke-width="1.5">
        <circle cx="309" cy="139" r="3" stroke="#333"/><circle cx="411" cy="149" r="3" stroke="var(--red)"/>
        <circle cx="299" cy="219" r="3" stroke="#333"/><circle cx="412" cy="223" r="3" stroke="var(--red)"/>
      </g>
    </svg>
    <div class="seg left sg1"><h4>Your Awesome Title One</h4><p>Lorem ipsum dolor sit amet, consectetur adipiscing elit, sed do eiusmod tempor incididunt ut labore et dolore magna aliqua.</p></div>
    <div class="seg right sg2"><h4>Your Awesome Title One</h4><p>Lorem ipsum dolor sit amet, consectetur adipiscing elit, sed do eiusmod tempor incididunt ut labore et dolore magna aliqua.</p></div>
    <div class="seg left sg3"><h4>Your Awesome Title One</h4><p>Lorem ipsum dolor sit amet, consectetur adipiscing elit, sed do eiusmod tempor incididunt ut labore et dolore magna aliqua.</p></div>
    <div class="seg right sg4"><h4>Your Awesome Title One</h4><p>Lorem ipsum dolor sit amet, consectetur adipiscing elit, sed do eiusmod tempor incididunt ut labore et dolore magna aliqua.</p></div>
    <footer class="footer"><svg width="712" height="25"><rect width="712" height="25" fill="var(--red)"/><polygon points="584,0 597,0 622,25 609,25" fill="#fff"/><polygon points="597,0 712,0 712,25 622,25" fill="var(--footer-dark)"/></svg><span class="copy">Copyright text here</span><span class="page">Page : 01</span></footer>
  </section>

  <section class="slide s6">
    <h2 class="slide-title">SECTION <span>TITLE HERE</span></h2>
    <div class="brand"><i></i>KEENLINE</div>
    <div class="row r1">
      <svg class="tag" width="46" height="82"><polygon points="0,41 26,0 46,0 46,82 26,82" fill="var(--red)"/></svg>
      <div class="tag"><span>01</span></div>
      <div class="panel"><h5>Your Awesome Title One</h5><p>Lorem ipsum dolor sit amet, consectetur adipiscing elit, sed do eiusmod tempor incididunt ut labore et dolore magna aliqua.<br>Lorem ipsum dolor sit amet, consectetur adipiscing elit, sed do eiusmod tempor incididunt ut labore et dolore magna aliqua.<br>Lorem ipsum dolor sit amet, consectetur adipiscing elit</p></div>
    </div>
    <div class="row r2">
      <svg class="tag" width="46" height="82"><polygon points="0,41 26,0 46,0 46,82 26,82" fill="#a84a4a"/></svg>
      <div class="tag"><span>02</span></div>
      <div class="panel"><h5>Your Awesome Title One</h5><p>Lorem ipsum dolor sit amet, consectetur adipiscing elit, sed do eiusmod tempor incididunt ut labore et dolore magna aliqua.<br>Lorem ipsum dolor sit amet, consectetur adipiscing elit, sed do eiusmod tempor incididunt ut labore et dolore magna aliqua.<br>Lorem ipsum dolor sit amet, consectetur adipiscing elit</p></div>
    </div>
    <div class="row r3">
      <svg class="tag" width="46" height="82"><polygon points="0,41 26,0 46,0 46,82 26,82" fill="#4a5058"/></svg>
      <div class="tag"><span>03</span></div>
      <div class="panel"><h5>Your Awesome Title One</h5><p>Lorem ipsum dolor sit amet, consectetur adipiscing elit, sed do eiusmod tempor incididunt ut labore et dolore magna aliqua.<br>Lorem ipsum dolor sit amet, consectetur adipiscing elit, sed do eiusmod tempor incididunt ut labore et dolore magna aliqua.<br>Lorem ipsum dolor sit amet, consectetur adipiscing elit</p></div>
    </div>
    <footer class="footer"><svg width="712" height="25"><rect width="712" height="25" fill="var(--red)"/><polygon points="584,0 597,0 622,25 609,25" fill="#fff"/><polygon points="597,0 712,0 712,25 622,25" fill="var(--footer-dark)"/></svg><span class="copy">Copyright text here</span><span class="page">Page : 01</span></footer>
  </section>

</div>
</body>
</html>
```